Business card and company stationary - Bravora Cleaning Ltd

1. Who are we and who are our customers?

o We are a relatively new cleaning company, established December 2008. We are a small company. We have 24 staff and we offer domestic and commercial cleaning services.
o We both (me and my wife) have been working for many years in the cleaning industry. We worked for some of the biggest and best cleaning companies in UK. We’ve been operatives, supervisors and managers.
o Inevitably after so many years of working for someone else, we decided to start our own business.
o Our domestic customers are middle class families and busy professionals. We’ve got some commercial customers, mainly offices.
o We are growing steadily.

2. What do we do? What are our services?

o Cleaning. We’ve got range of services - not to many but still can be daunting and confusing for some.
o Generally we’ve got domestic and commercial clients. The approach to the domestic cleaning customers is different to the commercial. In the way we want to say that it is cleaning that we do, but we acknowledge the environment and we appreciate the personal circumstances and requirements that are present. We do care, we listen and we try to work out the best possible way to complete our work.
o Mainly we get our work through referrals

3. What do we want with our stationery ?

o To place and maintain our message and reach out to people and organisations
o We want to advertise, communicate and sale.
o We are going to sell services.
o Increase membership, loyalty and support.

We are after business card design, headed letter and compliment slip.
We would like the headed letter to be created in formats suitable for :
- printing format
- also for use in our daily correspondence via e mail with clients and staff in a easy to edit and write format

The website we have is still under contraction and the domain is bravoracleaning.example

Target Market(s)

Families, individuals, businesses.

Industry/Entity Type

Cleaning Service

Contact Information for Business Card

FRONT :
Company Name - Bravora Cleaning Ltd
Company address - 41 Pelgate Rd, Hornchurch, Essex, RM14 7QD
Name - Mrs. Radoslava Petkova - Sola
Title - Managing Director
Company phone - 020 8937 2158
E mail - sola.petkova@bravoracleaning.example

BACK :

Company website - bravoracleaning.example
E mail - enquiries@bravoracleaning.example

Font styles to use
Serif

Requirements
Must have
• The above items and company logo...maybe at the back. But I'm free for any suggestions.

```html
<!DOCTYPE html>
<html lang="en">
<head>
<meta charset="utf-8">
<title>Bravora Cleaning Ltd — Business Card</title>
<link href="https://fonts.googleapis.com/css2?family=Open+Sans:wght@300;400;600;800&display=swap" rel="stylesheet">
<style>
  :root {
    --sky: #4bb8e8;
    --sky-light: #8fd3f2;
    --ink: #1d1d1b;
    --grey: #5a5a5a;
    --paper: #ffffff;
    --backdrop: #e9e6e1;
    --rule: #c9c9c9;
  }
  * { box-sizing: border-box; margin: 0; padding: 0; }
  html, body {
    width: 1200px; height: 950px; overflow: hidden;
    background: var(--backdrop);
    font-family: "Open Sans", Arial, sans-serif;
  }
  .canvas {
    position: relative; width: 1200px; height: 950px;
  }
  .card {
    position: absolute; left: 250px; width: 700px; height: 400px;
    box-shadow: 0 6px 18px rgba(0,0,0,.18);
    overflow: hidden;
  }
  /* Front */
  .card-front { top: 50px; background: var(--paper); }
  .front-band {
    position: absolute; left: 0; right: 0; top: 0; height: 78px;
    background: var(--sky);
  }
  .front-band::after {
    content: ""; position: absolute; left: 0; right: 0; bottom: -14px; height: 6px;
    background: var(--sky-light);
  }
  .front-body {
    position: absolute; left: 0; right: 0; top: 100px; bottom: 0;
    display: flex; align-items: center;
  }
  .identity {
    flex: 0 0 360px; display: flex; flex-direction: column; align-items: center;
    text-align: center;
  }
  .brand {
    display: flex; align-items: center; gap: 14px; margin-bottom: 26px;
  }
  .brand-dot {
    width: 58px; height: 58px; border-radius: 50%;
    border: 3px solid var(--ink); background: var(--paper);
  }
  .brand-name {
    font-weight: 800; font-size: 24px; letter-spacing: 1px;
    color: var(--sky); line-height: 1.1; text-transform: uppercase; text-align: left;
  }
  .person-name {
    font-weight: 400; font-size: 19px; color: var(--sky); letter-spacing: 1px;
    text-transform: uppercase;
  }
  .person-title { font-size: 15px; color: var(--ink); margin-top: 4px; }
  .address { font-size: 14px; color: var(--grey); margin-top: 18px; line-height: 1.5; }
  .divider { width: 1px; height: 200px; background: var(--rule); }
  .contacts {
    list-style: none; padding-left: 40px; font-size: 15px; color: var(--ink);
  }
  .contacts li { display: flex; align-items: center; gap: 12px; margin: 9px 0; }
  .contacts svg { width: 16px; height: 16px; fill: var(--sky); flex: none; }
  /* Back */
  .card-back { top: 500px; background: var(--sky); }
  .back-brand {
    position: absolute; left: 0; right: 0; top: 130px;
    display: flex; align-items: center; justify-content: center; gap: 22px;
  }
  .back-dot {
    width: 90px; height: 90px; border-radius: 50%;
    background: var(--paper); border: 5px solid var(--ink);
  }
  .back-name {
    font-weight: 800; font-size: 40px; letter-spacing: 2px; color: var(--ink);
    text-transform: uppercase; line-height: 1.05;
  }
  .back-web {
    position: absolute; left: 0; right: 0; bottom: 60px; text-align: center;
    font-size: 17px; color: var(--paper); letter-spacing: 1px;
  }
</style>
</head>
<body>
<main class="canvas">

  <section class="card card-front" aria-label="Business card front">
    <div class="front-band"></div>
    <div class="front-body">
      <div class="identity">
        <div class="brand">
          <span class="brand-dot"></span>
          <span class="brand-name">Bravora<br>Cleaning Ltd</span>
        </div>
        <p class="person-name">Marek Halloway</p>
        <p class="person-title">CEO/Founder</p>
        <p class="address">41 Pelgate Rd<br>Hornchurch, Essex RM14 7QD</p>
      </div>
      <div class="divider"></div>
      <ul class="contacts">
        <li><svg viewBox="0 0 16 16"><path d="M3 1l3 3-2 2c1 2 3 4 5 5l2-2 3 3-2 3C6 15 1 10 0 4z"/></svg>020 8937 2158</li>
        <li><svg viewBox="0 0 16 16"><path d="M4 0h8a1 1 0 011 1v14a1 1 0 01-1 1H4a1 1 0 01-1-1V1a1 1 0 011-1zm1 2v10h6V2z"/></svg>020 8937 2274</li>
        <li><svg viewBox="0 0 16 16"><path d="M4 0h8v4H4zM1 5h14v7h-3v4H4v-4H1zm4 5v4h6v-4z"/></svg>020 8937 2390</li>
        <li><svg viewBox="0 0 16 16"><path d="M0 3h16v10H0zm1 1v1l7 4 7-4V4z"/></svg>hello@bravoracleaning.example</li>
        <li><svg viewBox="0 0 16 16"><circle cx="8" cy="8" r="7.5"/></svg>www.bravoracleaning.example</li>
      </ul>
    </div>
  </section>

  <section class="card card-back" aria-label="Business card back">
    <div class="back-brand">
      <span class="back-dot"></span>
      <span class="back-name">Bravora<br>Cleaning Ltd</span>
    </div>
    <p class="back-web">www.bravoracleaning.example</p>
  </section>

</main>
</body>
</html>
```